Innovative Business Card Design

we are a bottled water factory
i am looking for an innovative business card idea
information on business card
shall be as per attachment sample ( Name , Number , ETC ..... )

```html
<!DOCTYPE html>
<html lang="en">
<head>
<meta charset="UTF-8">
<title>Clarelle Business Card</title>
<link rel="stylesheet" href="https://fonts.googleapis.com/css2?family=Montserrat:wght@500&family=Tinos&display=swap">
<style>
  :root {
    --page-bg: #d6d7d9;
    --card-white: #ffffff;
    --brand-navy: #2b2474;
    --card-blue: #1f2b91;
    --text-light: #e6e9ff;
    --water-deep: #2f4f86;
    --water-mid: #6f93c4;
    --water-light: #c9daee;
  }
  * { margin: 0; padding: 0; box-sizing: border-box; }
  html, body {
    width: 1200px;
    height: 900px;
    overflow: hidden;
    background: var(--page-bg);
  }
  .card {
    position: absolute;
    left: 290px;
    width: 620px;
    height: 354px;
    overflow: hidden;
    box-shadow: 0 6px 18px rgba(0, 0, 0, 0.18);
  }
  .card-front {
    top: 60px;
    background: var(--card-white);
  }
  .card-back {
    top: 486px;
    background: var(--card-blue);
  }
  .wordmark {
    position: absolute;
    top: 112px;
    left: 0;
    width: 100%;
    text-align: center;
    font-family: "Montserrat", sans-serif;
    font-weight: 500;
    font-size: 30px;
    letter-spacing: 4px;
    color: var(--brand-navy);
  }
  .water-visual {
    position: absolute;
    left: 0;
    bottom: 0;
    width: 100%;
    height: 168px;
    background:
      linear-gradient(180deg,
        rgba(255, 255, 255, 1) 0%,
        var(--water-light) 18%,
        var(--water-mid) 42%,
        var(--water-deep) 62%,
        var(--water-mid) 80%,
        var(--water-light) 100%);
  }
  .holder-name {
    position: absolute;
    top: 26px;
    left: 0;
    width: 100%;
    text-align: center;
    font-family: "Tinos", serif;
    font-size: 17px;
    color: var(--text-light);
  }
  .contact-list {
    position: absolute;
    left: 44px;
    top: 188px;
    list-style: none;
    font-family: "Tinos", serif;
    font-size: 15px;
    line-height: 24px;
    color: var(--text-light);
  }
  .contact-item {
    display: flex;
    align-items: center;
    gap: 8px;
  }
  .contact-icon {
    width: 12px;
    height: 12px;
    fill: var(--text-light);
  }
</style>
</head>
<body>
  <section class="card card-front">
    <div class="wordmark">CLARELLE</div>
    <div class="water-visual" role="img" aria-label="Photograph of splashing clear blue water with bubbles"></div>
  </section>

  <section class="card card-back">
    <div class="holder-name">Omar Halden</div>
    <ul class="contact-list">
      <li class="contact-item">14/3B Cedar Lane, Riverside</li>
      <li class="contact-item">
        <svg class="contact-icon" viewBox="0 0 24 24" aria-hidden="true">
          <path d="M6.6 10.8a15.1 15.1 0 0 0 6.6 6.6l2.2-2.2a1 1 0 0 1 1-.25 11.4 11.4 0 0 0 3.6.57 1 1 0 0 1 1 1V20a1 1 0 0 1-1 1A17 17 0 0 1 3 4a1 1 0 0 1 1-1h3.5a1 1 0 0 1 1 1c0 1.25.2 2.45.57 3.57a1 1 0 0 1-.25 1z"/>
        </svg>
        +00 123 456 789
      </li>
    </ul>
  </section>
</body>
</html>
```